Pondmentor: an app for coaches and students in golf and fitness

I currently have an app that is called Pondmentor and I am redoing the app completely and with this I am looking for a cool design for the app. I am not happy with the design as it is at the moment. The app should have a nice welcome and when you are logged in the dashboard must be very modern. It is a golf app that have 2 type of users. 1 user is the coach and the other user is the student. Those users can see different things of course.
The coach is normally paying a subscription charge for using the app but I want to get the students to pay for different tools that I will be offering via the app. To me the dashboard and the homepage of the app (once you have downloaded the app) is important. Here I would like to get the student as well as the coach the feeling of what the app can offer. The app offers features like Calendar (here the student can book the coach via the calendar), Chat (here the coach and the student can chat with each other as well as the coach can creat group chats with several students), Notes (here the coach as well as the student can create notes for their lessons), video tips (here the coach can upload video tips for his/her students, online lesson (the student can take online lessons by uploading recorded videos..and so on

Target Market(s)

Sport coaches (for start it will be mostly golf coaches)

Industry/Entity Type

Sports

Font styles to use
Sans Serif

Colors
0054AA
0677BA
7BADD7
CADEEF
E8F1F8

Requirements
Must have
• modern design and easy navigation.
Nice to have
• It all starts with the dashboard
Should not have
• boring standard style.

```html
<!DOCTYPE html>
<html lang="en">
<head>
<meta charset="utf-8">
<title>Pondmentor – App Screens</title>
<link href="https://fonts.googleapis.com/css2?family=Raleway:wght@400;500;600;700;800&display=swap" rel="stylesheet">
<style>
:root{
  --navy:#0054AA;
  --blue:#0677BA;
  --sky:#7BADD7;
  --mist:#CADEEF;
  --ice:#E8F1F8;
  --dash-bg:#D5E5F2;
  --dim-body:#8CB2D8;
  --dim-cell:#A6C4E3;
  --dim-title:#A3C3E6;
  --ink:#1B1B1B;
  --muted:#555;
  --sys:#7BADD7;
  --sys-dim:#3C75B6;
}
*{box-sizing:border-box;margin:0;padding:0}
html,body{width:1200px;height:990px;overflow:hidden}
body{font-family:'Raleway',sans-serif;background:#777}
.stage{position:relative;width:1440px;height:1188px;transform:scale(.833333);transform-origin:0 0;
  background:radial-gradient(ellipse at 50% 45%,#4a4a4a 0%,#6b6b6b 45%,#8a8a8a 100%);overflow:hidden}
.wave{position:absolute;inset:0}
.phone{position:absolute;top:160px;width:375px;height:868px;overflow:hidden}
.p1{left:111px;background:var(--dash-bg)}
.p2{left:533px;background:var(--dim-body)}
.p3{left:954px;background:var(--dim-body)}
.app-bar{height:84px;background:var(--navy);display:flex;align-items:center;justify-content:center;
  font-weight:800;font-size:37px;color:#fff;letter-spacing:.2px}
.dim .app-bar{color:var(--dim-title)}
.sub-bar{height:52px;background:var(--blue);display:flex;align-items:center;padding-left:38px;gap:18px;
  color:#fff;font-weight:700;font-size:26px}
.dim .sub-bar{background:#2E7CC0;color:var(--dim-title)}
.burger{width:22px;height:18px;display:flex;flex-direction:column;justify-content:space-between}
.burger i{display:block;height:3px;background:currentColor}
.tile{position:absolute;width:173px;height:202px;background:#fff;border:1px solid var(--mist);border-radius:8px;
  text-align:center;padding-top:18px}
.tile svg{width:40px;height:40px;stroke:var(--navy);fill:none;stroke-width:2}
.tile h3{font-size:20px;font-weight:700;color:var(--ink);margin-top:14px}
.tile p{font-size:15px;line-height:23px;color:var(--muted);margin:12px 8px 0}
.tile.active{background:linear-gradient(180deg,#AACDEB 0%,#3D7BBF 100%);border:none}
.tile.active svg{stroke:#fff}
.tile.active h3,.tile.active p{color:#fff}
.sys-nav{position:absolute;left:0;right:0;bottom:0;height:84px;display:flex;justify-content:center;align-items:center;gap:64px}
.sys-nav svg{width:28px;height:28px;fill:var(--sys)}
.dim .sys-nav svg{fill:var(--sys-dim)}
.day-head{position:absolute;top:164px;font-size:14px;color:#2a3d55}
.hour{position:absolute;left:13px;font-size:13px;font-weight:700;color:#1f3550}
.grid{position:absolute;left:65px;top:196px;width:297px;border-collapse:collapse}
.grid td{border:1px solid var(--sky);background:var(--dim-cell);height:41.5px;padding:0}
.tool-bar{position:absolute;left:0;right:0;top:740px;height:44px;background:var(--navy)}
.tool-bar svg{position:absolute;top:14px;width:16px;height:16px;fill:#8FB7E2}
.picker{position:absolute;left:15px;top:389px;width:345px;height:289px;background:#fff;border-radius:6px;box-shadow:0 4px 14px rgba(0,0,0,.2)}
.picker-head{position:absolute;left:52px;top:0;width:242px;height:32px;background:var(--navy);color:#fff;
  font-weight:600;font-size:14px;display:flex;align-items:center;justify-content:center}
.picker-head span{position:absolute;top:5px;width:22px;height:22px;border-radius:50%;background:#fff;color:var(--navy);
  font-size:14px;display:flex;align-items:center;justify-content:center}
.cal-cell{position:absolute;width:30px;margin-left:-15px;text-align:center;font-size:11px;color:#222}
.cal-cell.wk{font-weight:700;font-size:11px}
.cal-cell.out{color:#ccc}
.cal-cell.sel{background:#3D8FDB;color:#fff;border-radius:50%;height:26px;line-height:26px;width:26px;margin-left:-13px;margin-top:-7px}
.view-menu{position:absolute;left:82px;top:451px;width:212px;height:289px;background:#fff;border-radius:6px;box-shadow:0 4px 14px rgba(0,0,0,.2)}
.view-item{position:absolute;left:52px;font-size:15px;font-weight:600;color:#111;width:110px;display:flex;justify-content:space-between}
.view-item b{font-weight:400}
</style>
</head>
<body>
<div class="stage">
  <svg class="wave" width="1440" height="1188" viewBox="0 0 1440 1188"><path d="M0 938 C420 928 900 950 1440 1022 L1440 1188 L0 1188 Z" fill="#0054AA"/></svg>

  <!-- Dashboard screen -->
  <section class="phone p1">
    <header class="app-bar">PONDMENTOR</header>
    <div class="sub-bar"><span class="burger"><i></i><i></i><i></i></span>Dashboard</div>

    <div class="tile active" style="left:10px;top:146px">
      <svg viewBox="0 0 40 40"><rect x="4" y="7" width="32" height="29" rx="3"/><line x1="4" y1="14" x2="36" y2="14"/><line x1="12" y1="3" x2="12" y2="10"/><line x1="28" y1="3" x2="28" y2="10"/></svg>
      <h3>My Calendar</h3><p>Book and manage your appointments 24/7</p>
    </div>
    <div class="tile" style="left:193px;top:146px">
      <svg viewBox="0 0 40 40"><rect x="3" y="9" width="24" height="22" rx="3"/><path d="M27 17 L37 10 L37 30 L27 23"/></svg>
      <h3>Online Lessons</h3><p>Edit and view your students online lessons</p>
    </div>
    <div class="tile" style="left:10px;top:359px">
      <svg viewBox="0 0 40 40"><circle cx="20" cy="12" r="8"/><path d="M4 38 V34 C4 27 9 24 20 24 C31 24 36 27 36 34 V38 Z"/></svg>
      <h3>My Products</h3><p>Configure lessons detail for calendar and online lesson</p>
    </div>
    <div class="tile" style="left:193px;top:359px">
      <svg viewBox="0 0 48 40" style="width:48px"><circle cx="24" cy="10" r="7"/><circle cx="10" cy="14" r="5"/><circle cx="38" cy="14" r="5"/><path d="M12 36 C12 25 17 21 24 21 C31 21 36 25 36 36 Z"/><path d="M2 32 C2 24 5 21 11 21"/><path d="M46 32 C46 24 43 21 37 21"/></svg>
      <h3>My Students</h3><p>Find all info of your students</p>
    </div>
    <div class="tile" style="left:10px;top:571px">
      <svg viewBox="0 0 40 40"><path d="M6 30 L28 8 L33 13 L11 35 L5 36 Z"/><line x1="25" y1="11" x2="30" y2="16"/></svg>
      <h3>Video Editor</h3><p>Excepteur sint occaecat cupidatat non proident</p>
    </div>
    <div class="tile" style="left:193px;top:571px">
      <svg viewBox="0 0 40 40"><path d="M8 3 H24 L33 12 V37 H8 Z"/><path d="M24 3 V12 H33"/></svg>
      <h3>Pond365</h3><p>Excepteur sint occaecat cupidatat non proident</p>
    </div>

    <nav class="sys-nav">
      <svg viewBox="0 0 28 28"><path d="M2 14 L24 3 V25 Z"/></svg>
      <svg viewBox="0 0 28 28"><circle cx="14" cy="14" r="13"/></svg>
      <svg viewBox="0 0 28 28"><rect x="1" y="1" width="26" height="26"/></svg>
    </nav>
  </section>

  <!-- Calendar with month picker -->
  <section class="phone p2 dim">
    <header class="app-bar">PONDMENTOR</header>
    <div class="sub-bar"><span class="burger"><i></i><i></i><i></i></span>Aug 29 - 31 2019</div>
    <span class="day-head" style="left:71px">Thu 29/08</span>
    <span class="day-head" style="left:182px">Fri 29/08</span>
    <span class="day-head" style="left:292px">Sat 29/08</span>
    <span class="hour" style="top:194px">12AM</span><span class="hour" style="top:239px">1AM</span>
    <span class="hour" style="top:283px">2AM</span><span class="hour" style="top:328px">3AM</span>
    <span class="hour" style="top:372px">4AM</span>
    <table class="grid"><colgroup><col style="width:93px"><col style="width:110px"><col></colgroup>
      <tr><td></td><td></td><td></td></tr><tr><td></td><td></td><td></td></tr><tr><td></td><td></td><td></td></tr>
      <tr><td></td><td></td><td></td></tr><tr><td></td><td></td><td></td></tr>
    </table>

    <div class="picker">
      <div class="picker-head"><span style="left:14px">&larr;</span>AUGUST 2019<span style="right:12px">&rarr;</span></div>
      <span class="cal-cell wk" style="left:30px;top:72px">MO</span><span class="cal-cell wk" style="left:77px;top:72px">TUE</span>
      <span class="cal-cell wk" style="left:125px;top:72px">WED</span><span class="cal-cell wk" style="left:172px;top:72px">THU</span>
      <span class="cal-cell wk" style="left:219px;top:72px">FRI</span><span class="cal-cell wk" style="left:266px;top:72px">SAT</span>
      <span class="cal-cell wk" style="left:313px;top:72px">SUN</span>

      <span class="cal-cell out" style="left:26px;top:109px">31</span><span class="cal-cell" style="left:70px;top:109px">1</span>
      <span class="cal-cell" style="left:115px;top:109px">2</span><span class="cal-cell" style="left:163px;top:109px">3</span>
      <span class="cal-cell" style="left:214px;top:109px">4</span><span class="cal-cell" style="left:259px;top:109px">5</span>
      <span class="cal-cell" style="left:305px;top:109px">6</span>

      <span class="cal-cell" style="left:24px;top:143px">7</span><span class="cal-cell" style="left:70px;top:143px">8</span>
      <span class="cal-cell" style="left:115px;top:143px">9</span><span class="cal-cell" style="left:167px;top:143px">10</span>
      <span class="cal-cell" style="left:217px;top:143px">11</span><span class="cal-cell" style="left:262px;top:143px">12</span>
      <span class="cal-cell" style="left:308px;top:143px">13</span>

      <span class="cal-cell" style="left:27px;top:177px">14</span><span class="cal-cell" style="left:74px;top:177px">15</span>
      <span class="cal-cell sel" style="left:118px;top:177px">16</span><span class="cal-cell" style="left:167px;top:177px">17</span>
      <span class="cal-cell" style="left:217px;top:177px">18</span><span class="cal-cell" style="left:262px;top:177px">19</span>
      <span class="cal-cell" style="left:308px;top:177px">20</span>

      <span class="cal-cell" style="left:27px;top:211px">21</span><span class="cal-cell" style="left:74px;top:211px">22</span>
      <span class="cal-cell" style="left:118px;top:211px">23</span><span class="cal-cell" style="left:167px;top:211px">24</span>
      <span class="cal-cell" style="left:217px;top:211px">25</span><span class="cal-cell" style="left:262px;top:211px">26</span>
      <span class="cal-cell" style="left:308px;top:211px">27</span>

      <span class="cal-cell" style="left:27px;top:245px">28</span><span class="cal-cell" style="left:74px;top:245px">29</span>
      <span class="cal-cell" style="left:118px;top:245px">30</span><span class="cal-cell out" style="left:167px;top:245px">31</span>
      <span class="cal-cell out" style="left:214px;top:245px">1</span><span class="cal-cell out" style="left:259px;top:245px">2</span>
      <span class="cal-cell out" style="left:305px;top:245px">3</span>
    </div>

    <div class="tool-bar">
      <svg style="left:66px" viewBox="0 0 16 16"><path d="M11 3 L5 8 L11 13 Z"/></svg>
      <svg style="left:115px" viewBox="0 0 16 16"><path d="M1 8 C4 3 12 3 15 8 C12 13 4 13 1 8 Z M8 5.5 A2.5 2.5 0 1 0 8 10.5 A2.5 2.5 0 1 0 8 5.5 Z" fill-rule="evenodd"/></svg>
      <svg style="left:178px" viewBox="0 0 16 16"><path d="M2 4 H14 V15 H2 Z M4 1 H6 V5 H4 Z M10 1 H12 V5 H10 Z"/></svg>
      <svg style="left:247px" viewBox="0 0 16 16"><path d="M7 1 H9 L9.5 3.2 L11.5 4 L13.3 2.7 L14.7 4.1 L13.5 6 L14.2 8 L15 8 L15 9 L13 9.5 L12.2 11.5 L13.3 13.3 L11.9 14.7 L10 13.5 L9 14 L9 15 L7 15 L6.5 12.8 L4.5 12 L2.7 13.3 L1.3 11.9 L2.5 10 L1.8 9 L1 9 L1 7 L3.2 6.5 L4 4.5 L2.7 2.7 L4.1 1.3 L6 2.5 Z M8 6 A2 2 0 1 0 8 10 A2 2 0 1 0 8 6 Z" fill-rule="evenodd"/></svg>
      <svg style="left:294px" viewBox="0 0 16 16"><path d="M5 3 L11 8 L5 13 Z"/></svg>
    </div>
    <nav class="sys-nav">
      <svg viewBox="0 0 28 28"><path d="M2 14 L24 3 V25 Z"/></svg>
      <svg viewBox="0 0 28 28"><circle cx="14" cy="14" r="13"/></svg>
      <svg viewBox="0 0 28 28"><rect x="1" y="1" width="26" height="26"/></svg>
    </nav>
  </section>

  <!-- Calendar with view menu -->
  <section class="phone p3 dim">
    <header class="app-bar">PONDMENTOR</header>
    <div class="sub-bar"><span class="burger"><i></i><i></i><i></i></span>Aug 29 - 31 2019</div>
    <span class="day-head" style="left:71px">Thu 29/08</span>
    <span class="day-head" style="left:182px">Fri 29/08</span>
    <span class="day-head" style="left:292px">Sat 29/08</span>
    <span class="hour" style="top:194px">12AM</span><span class="hour" style="top:239px">1AM</span>
    <span class="hour" style="top:283px">2AM</span><span class="hour" style="top:328px">3AM</span>
    <span class="hour" style="top:372px">4AM</span><span class="hour" style="top:417px">5AM</span>
    <span class="hour" style="top:461px">6AM</span><span class="hour" style="top:506px">7AM</span>
    <span class="hour" style="top:550px">8AM</span><span class="hour" style="top:595px">9AM</span>
    <span class="hour" style="top:639px">10AM</span>
    <table class="grid"><colgroup><col style="width:93px"><col style="width:110px"><col></colgroup>
      <tr><td></td><td></td><td></td></tr><tr><td></td><td></td><td></td></tr><tr><td></td><td></td><td></td></tr>
      <tr><td></td><td></td><td></td></tr><tr><td></td><td></td><td></td></tr><tr><td></td><td></td><td></td></tr>
      <tr><td></td><td></td><td></td></tr><tr><td></td><td></td><td></td></tr><tr><td></td><td></td><td></td></tr>
      <tr><td></td><td></td><td></td></tr><tr><td></td><td></td><td></td></tr>
    </table>

    <div class="view-menu">
      <div class="view-item" style="top:36px">Month<b>&rarr;</b></div>
      <div class="view-item" style="top:76px">Week<b>&rarr;</b></div>
      <div class="view-item" style="top:116px">3 Days<b>&rarr;</b></div>
      <div class="view-item" style="top:156px">Day<b>&rarr;</b></div>
      <div class="view-item" style="top:196px">Today<b>&rarr;</b></div>
      <div class="view-item" style="top:236px">List<b>&rarr;</b></div>
    </div>

    <div class="tool-bar">
      <svg style="left:66px" viewBox="0 0 16 16"><path d="M11 3 L5 8 L11 13 Z"/></svg>
      <svg style="left:115px" viewBox="0 0 16 16"><path d="M1 8 C4 3 12 3 15 8 C12 13 4 13 1 8 Z M8 5.5 A2.5 2.5 0 1 0 8 10.5 A2.5 2.5 0 1 0 8 5.5 Z" fill-rule="evenodd"/></svg>
      <svg style="left:178px" viewBox="0 0 16 16"><path d="M2 4 H14 V15 H2 Z M4 1 H6 V5 H4 Z M10 1 H12 V5 H10 Z"/></svg>
      <svg style="left:247px" viewBox="0 0 16 16"><path d="M7 1 H9 L9.5 3.2 L11.5 4 L13.3 2.7 L14.7 4.1 L13.5 6 L14.2 8 L15 8 L15 9 L13 9.5 L12.2 11.5 L13.3 13.3 L11.9 14.7 L10 13.5 L9 14 L9 15 L7 15 L6.5 12.8 L4.5 12 L2.7 13.3 L1.3 11.9 L2.5 10 L1.8 9 L1 9 L1 7 L3.2 6.5 L4 4.5 L2.7 2.7 L4.1 1.3 L6 2.5 Z M8 6 A2 2 0 1 0 8 10 A2 2 0 1 0 8 6 Z" fill-rule="evenodd"/></svg>
      <svg style="left:294px" viewBox="0 0 16 16"><path d="M5 3 L11 8 L5 13 Z"/></svg>
    </div>
    <nav class="sys-nav">
      <svg viewBox="0 0 28 28"><path d="M2 14 L24 3 V25 Z"/></svg>
      <svg viewBox="0 0 28 28"><circle cx="14" cy="14" r="13"/></svg>
      <svg viewBox="0 0 28 28"><rect x="1" y="1" width="26" height="26"/></svg>
    </nav>
  </section>
</div>
</body>
</html>
```